Polystyrene Environmental Synopsis

We need a fact sheet for quick reference that groups information units and has a simple but engaging visual presentation of the text and various infographics. We are a trade association representing polystyrene foam manufacturers and this piece is intended to help our members provide effective messaging to their sales personnel.

To view our typical company design/style please see our website at www.foamtradeunion.org. Our primary RGB colors are: (187,140,9); (94,47,29); (94,138,164); and (164,167,15). Secondary RGB colors are (249,162,28) and (218,210,208). Our title/header font is DIN Next LT Pro and our copy font is Calibri 10.5 pt. We can deviate from the font specification if beneficial.

Target Market(s)

Polystyrene manufacturer plant workers and other employees.

Font styles to use
Sans Serif

Requirements
Must have
• Information presentation must be clean and easy to reference.

```html
<!DOCTYPE html>
<html lang="en">
<head>
<meta charset="utf-8">
<title>Foam Trade Union – Talking Points</title>
<link rel="stylesheet" href="https://fonts.googleapis.com/css2?family=Oswald:wght@400;500;600;700&family=Carlito:ital,wght@0,400;0,700;1,700&family=Barlow+Semi+Condensed:wght@600&display=swap">
<style>
:root{
  --gold:#bb8c09;
  --brown:#5e2f1d;
  --blue:#5e8aa4;
  --olive:#a4a70f;
  --orange:#f9a21c;
  --stone:#dad2d0;
  --backdrop:#555a5d;
  --panel:#e4e4e4;
  --panel-dark:#dcdcdc;
  --bar:#7a6e6a;
  --ink:#3a3a3a;
  --title-gray:#707070;
}
*{box-sizing:border-box;margin:0;padding:0}
html,body{width:1200px;height:1200px;overflow:hidden;background:var(--backdrop)}
body{position:relative;font-family:"Carlito",Calibri,sans-serif;color:var(--ink)}

.sheet{position:absolute;top:176px;width:566px;height:732px;background:#fff;overflow:hidden}
.sheet--front{left:26px}
.sheet--back{left:610px}

/* masthead */
.masthead{position:absolute;left:0;top:0;width:566px;height:100px;background:var(--panel)}
.brand{position:absolute;left:0;top:8px;width:202px;height:82px;background:#fff;border-radius:0 41px 41px 0;display:flex;align-items:center;padding-left:22px;gap:8px}
.brand-dot{width:62px;height:62px;border-radius:50%;background:var(--gold);flex:none}
.brand-name{font-family:"Carlito",sans-serif;font-weight:400;font-size:15px;line-height:1.05;color:var(--brown);width:80px}
.headline{position:absolute;left:318px;top:6px;height:90px}
.headline-big{position:absolute;left:0;top:0;font-family:"Oswald",sans-serif;font-weight:700;font-size:66px;line-height:84px;color:var(--brown);letter-spacing:-1px}
.headline-small{position:absolute;left:104px;top:6px;font-family:"Oswald",sans-serif;font-weight:500;font-size:29px;line-height:34px;color:var(--title-gray);white-space:nowrap}
.headline-small span{display:block}
.headline-rule{position:absolute;left:104px;top:78px;width:150px;height:3px;background:var(--orange)}

/* side rails */
.rail{position:absolute;left:0;width:42px;display:flex;align-items:center;justify-content:center}
.rail-label{writing-mode:vertical-rl;transform:rotate(180deg);font-family:"Oswald",sans-serif;font-weight:500;font-size:25px;color:#fff;white-space:nowrap;letter-spacing:.2px}
.rail--intro{top:100px;height:320px;background:var(--orange)}
.rail--intro .rail-label{font-size:27px}
.rail--unit1{top:420px;height:258px;background:var(--olive)}
.rail--unit2{top:100px;height:286px;background:var(--brown)}
.rail--unit3{top:386px;height:292px;background:var(--gold)}

/* intro */
.lead{position:absolute;left:57px;top:106px;width:490px;font-size:8.7px;line-height:12px;font-style:italic;font-weight:700;color:#2a2a2a}
.section-title{position:absolute;left:54px;top:148px;font-family:"Barlow Semi Condensed",sans-serif;font-weight:600;font-size:20px;color:var(--brown);letter-spacing:.3px}
.section-title em{font-style:normal;border-bottom:3px solid var(--orange)}

.voice{position:absolute;left:308px;top:184px;width:248px;height:216px}
.voice-head{height:40px;background:var(--brown);border-radius:12px 12px 0 0;color:#fff;font-family:"Carlito",sans-serif;font-weight:700;font-size:10px;padding:9px 0 0 83px;white-space:nowrap}
.voice-head b{font-size:21px;font-family:"Oswald",sans-serif;font-weight:600;letter-spacing:.3px}
.voice-body{height:176px;background:var(--orange);border-radius:0 0 12px 12px;padding:10px 6px 0 83px;color:#fff}
.voice-quote{font-style:italic;font-weight:700;font-size:12px;line-height:15.5px;margin-bottom:12px}
.voice-copy{font-size:8.6px;line-height:11.6px}
.voice-tail{position:absolute;left:200px;top:212px}

.pointers{position:absolute;left:54px;top:196px;width:328px;height:194px;background:var(--panel-dark);border-radius:7px}
.pointers-head{height:17px;background:var(--bar);color:#fff;text-align:center;font-family:"Carlito",sans-serif;font-size:11px;line-height:17px;border-radius:7px 7px 0 0;letter-spacing:.3px}
.pointers-list{list-style:none;padding:5px 8px 0 20px;font-size:8.6px;line-height:11.6px}
.pointers-list li{position:relative}
.pointers-list li::before{content:"";position:absolute;left:-6px;top:4px;width:3px;height:3px;border-radius:50%;background:var(--orange)}
.pointers-tail{position:absolute;left:0;top:188px}

/* information units */
.unit-bg{position:absolute;left:42px;background:var(--panel)}
.pill{position:absolute;z-index:3;height:23px;border-radius:12px;color:#fff;text-align:center;font-family:"Oswald",sans-serif;font-weight:500;font-size:15.5px;line-height:19px;letter-spacing:.3px;border:2px solid #fff;box-shadow:0 0 0 1px rgba(0,0,0,.08)}
.pill--olive{background:var(--olive)}
.pill--gold{background:var(--gold)}
.pill--brown{background:var(--brown)}

.ledger{position:absolute;z-index:1}
.ledger-head{display:flex;background:var(--bar);color:#fff;font-family:"Carlito",sans-serif;font-size:11px;letter-spacing:.3px;align-items:center;padding-top:3px}
.ledger-head .col-fact{text-align:center}
.ledger-head .col-support{text-align:center;flex:1}
.ledger-rows{position:relative}
.ledger-row{position:relative;display:flex}
.ledger-row + .ledger-row .fact-cell,
.ledger-row + .ledger-row .support-cell{border-top:1px dotted #b9b3a6}
.fact-cell{flex:none;font-weight:700;color:var(--brown);font-size:8.6px;line-height:11.6px;padding-top:10px}
.support-cell{flex:1;padding:6px 6px 0 10px}
.support-cell ul{list-style:none;font-size:8.6px;line-height:11.6px}
.support-cell li{position:relative;padding-left:7px}
.support-cell li::before{content:"";position:absolute;left:0;top:4px;width:3px;height:3px;border-radius:50%;background:var(--marker,var(--olive))}
.divider{position:absolute;top:0;bottom:0;width:1.5px}
.badge{position:absolute;width:40px;height:40px;border-radius:50%;border:2px solid #fff;box-shadow:0 1px 3px rgba(0,0,0,.35);display:flex;align-items:center;justify-content:center}
.badge--brown{background:var(--brown)}
.badge--olive{background:var(--olive)}

/* footer */
.footer{position:absolute;left:0;top:678px;width:566px;height:54px;background:var(--blue);color:#fff;font-weight:700;font-size:8.6px;line-height:11.4px}
.footer-address{position:absolute;left:74px;top:10px}
.footer-contact{position:absolute;left:262px;top:10px}
.footer-pin{position:absolute;left:63px;top:19px}
.footer-icons{position:absolute;left:248px;top:11px}
.social{position:absolute;top:9px;width:34px;height:34px;border-radius:50%;background:var(--olive);border:2px solid #fff}
.social--a{left:471px}
.social--b{left:512px}
</style>
</head>
<body>

<!-- FRONT SHEET -->
<section class="sheet sheet--front">
  <header class="masthead">
    <div class="brand"><span class="brand-dot"></span><span class="brand-name">Foam Trade Union</span></div>
    <div class="headline">
      <span class="headline-big">EPS</span>
      <span class="headline-small"><span>TALKING</span><span>POINTS</span></span>
      <span class="headline-rule"></span>
    </div>
  </header>

  <div class="rail rail--intro"><span class="rail-label">INTRODUCTION</span></div>
  <div class="rail rail--unit1"><span class="rail-label">INFORMATION UNIT #1</span></div>

  <p class="lead">Polystyrene bans, recycling, and human health are TOP objections facing the EPS industry. When confronted with false allegations about EPS, here are some fast facts to help respond proactively.<br>Perfect for packaging conferences, social media, &amp; sales objectives.</p>

  <h2 class="section-title">POLYSTERENE <em>DEFENSE</em> LINE</h2>

  <aside class="voice">
    <div class="voice-head">HAVE A <b>BIGGER</b> VOICE!</div>
    <div class="voice-body">
      <p class="voice-quote">The more educated we are, the more educated others will be.</p>
      <p class="voice-copy">Share this document with your employees even if they do not deal directly with your customers or specific packaging audiences.<br>Everyone working within the EPS industry should be aware of the strong environmental profile for EPS.</p>
    </div>
    <svg class="voice-tail" width="48" height="28" viewBox="0 0 48 28"><path d="M0 0 L48 0 L44 26 Z" fill="var(--orange)"/></svg>
  </aside>

  <div class="pointers">
    <div class="pointers-head">MAKING YOUR POINT</div>
    <ul class="pointers-list">
      <li>Speaking with <b>confidence</b> means knowing your material.</li>
      <li>When responding to misstatements be prepared to challenge the source with <b>factual</b> information.</li>
      <li>Using a question format is <b>less confrontational</b>, e.g., “Did you know…” or “Were you aware…”?</li>
      <li>Make <b>affirmative statements</b> whenever possible; avoid restating the misinformation in your response.</li>
      <li>When addressing someone that refuses to give reasonable consideration to new information, we recommend responding, “It’s unfortunate you’re not willing to look into this further.”</li>
      <li>When given the opportunity to address an individual or an audience about EPS sustainability, <b>focus on three (3) specific talking points</b> to keep the discussion or presentation focused. Plan your talking points &amp; don’t deviate; this is an effective strategy for dealing with media inquiries as well.</li>
    </ul>
    <svg class="pointers-tail" width="70" height="26" viewBox="0 0 70 26"><path d="M12 0 L60 0 L0 24 Z" fill="var(--panel-dark)"/></svg>
  </div>

  <div class="unit-bg" style="top:420px;width:524px;height:258px"></div>
  <div class="pill pill--olive" style="left:213px;top:429px;width:204px">RECYCLING</div>

  <div class="ledger" style="left:72px;top:448px;width:479px;--marker:var(--olive)">
    <div class="ledger-head" style="height:24px"><span class="col-fact" style="width:119px">FACT</span><span class="col-support">SUPPORTING INFORMATION</span></div>
    <div class="ledger-rows" style="background:#fff">
      <span class="divider" style="left:119px;background:var(--olive)"></span>
      <div class="ledger-row" style="height:104px">
        <div class="badge badge--brown" style="left:-17px;top:8px">
          <svg width="22" height="22" viewBox="0 0 24 24" fill="none" stroke="#fff" stroke-width="2.4" stroke-linecap="round"><path d="M5 15 A8 8 0 0 1 9 5"/><path d="M15 5 A8 8 0 0 1 19 14"/><path d="M16 19 A8 8 0 0 1 7 19"/><path d="M7 3 L9 5 L7 8"/><path d="M21 12 L19 14 L16 13"/><path d="M9 21 L7 19 L9 16"/></svg>
        </div>
        <div class="fact-cell" style="width:119px;padding-left:40px;padding-top:22px">EPS is Recyclable</div>
        <div class="support-cell"><ul>
          <li>Historically, EPS recycling averages ~18% over a 25-year trendline.</li>
          <li>EPS recycling is most successful in commercial waste streams with large volume sources of EPS waste.</li>
          <li>Consumer access to EPS recycling sometimes requires extra effort, but with proper equipment &amp; handling, it is successful in many communities.</li>
          <li>Creative problem solving for challenging recycling scenarios means Northgate Foods, VitaBox, Harbor Kitchen, Coldline, Volt Depot, Prairie Steaks are committed to long term EPS recycling.</li>
        </ul></div>
      </div>
      <div class="ledger-row" style="height:48px">
        <div class="badge badge--brown" style="left:-17px;top:4px">
          <svg width="22" height="22" viewBox="0 0 24 24" fill="none" stroke="#fff" stroke-width="2.2"><circle cx="9" cy="9" r="4"/><circle cx="9" cy="9" r="6.5" stroke-dasharray="2.5 2"/><circle cx="17.5" cy="17" r="3.5"/></svg>
        </div>
        <div class="fact-cell" style="width:119px;padding-left:40px;padding-top:6px;padding-right:2px">New EPS Recycling Technologies Are Emerging</div>
        <div class="support-cell"><ul>
          <li>Pyrolisis—a chemical reprocessing method—increases the ability to recycle contaminated EPS waste.</li>
          <li>Two new facilities opened in 2018.</li>
        </ul></div>
      </div>
      <div class="ledger-row" style="height:47px">
        <div class="badge badge--brown" style="left:-17px;top:2px">
          <svg width="22" height="22" viewBox="0 0 24 24" fill="#fff"><rect x="3" y="16" width="4" height="6"/><rect x="9" y="12" width="4" height="10"/><rect x="15" y="8" width="4" height="14"/><path d="M3 12 L14 4 L13 2 L20 2 L18 8 L16 6 L4 14 Z"/></svg>
        </div>
        <div class="fact-cell" style="width:119px;padding-left:40px;padding-top:6px">EPS End-Markets Show Consistent Growth</div>
        <div class="support-cell"><ul>
          <li>It is used as recycled content in new EPS packaging and other EPS products.</li>
          <li>Markets for recycled content EPS include:<br>Crown Molding, Surfboards, Picture Frames, Other Rigid Polystyrene Applications</li>
        </ul></div>
      </div>
    </div>
  </div>

  <footer class="footer">
    <svg class="footer-pin" width="8" height="11" viewBox="0 0 8 11"><path d="M4 0 A4 4 0 0 1 8 4 C8 7 4 11 4 11 C4 11 0 7 0 4 A4 4 0 0 1 4 0 Z" fill="#fff"/><circle cx="4" cy="4" r="1.5" fill="var(--blue)"/></svg>
    <p class="footer-address">Foam Trade Union<br>4470 Meridian Avenue Suite 310<br>Linwood, MD 21077</p>
    <svg class="footer-icons" width="10" height="34" viewBox="0 0 10 34" fill="#fff"><path d="M2 0 L4 0 L5 3 L3.5 4 C4 6 5 7 6.5 7.5 L7.5 6 L10 7 L10 9 C5 9 1 5 1 1 Z"/><rect x="1" y="13" width="8" height="6" rx="1"/><rect x="3" y="11" width="4" height="3"/><circle cx="5" cy="28" r="4.5" fill="none" stroke="#fff" stroke-width="1.2"/><path d="M0.5 28 H9.5 M5 23.5 V32.5" stroke="#fff" stroke-width="1"/></svg>
    <p class="footer-contact">800.555.0142<br>410.555.0187<br>www.foamtradeunion.org</p>
    <span class="social social--a"></span>
    <span class="social social--b"></span>
  </footer>
</section>

<!-- BACK SHEET -->
<section class="sheet sheet--back">
  <header class="masthead">
    <div class="brand"><span class="brand-dot"></span><span class="brand-name">Foam Trade Union</span></div>
    <div class="headline">
      <span class="headline-big">EPS</span>
      <span class="headline-small"><span>TALKING</span><span>POINTS</span></span>
      <span class="headline-rule"></span>
    </div>
  </header>

  <div class="rail rail--unit2"><span class="rail-label">INFORMATION UNIT #2</span></div>
  <div class="rail rail--unit3"><span class="rail-label">INFORMATION UNIT #3</span></div>

  <div class="pill pill--gold" style="left:216px;top:117px;width:198px">EPS BANS</div>
  <div class="ledger" style="left:72px;top:136px;width:478px;--marker:var(--orange)">
    <div class="ledger-head" style="height:28px"><span class="col-fact" style="width:118px">FACT</span><span class="col-support">SUPPORTING INFORMATION</span></div>
    <div class="ledger-rows" style="background:var(--panel-dark)">
      <span class="divider" style="left:118px;top:6px;bottom:6px;background:var(--gold)"></span>
      <div class="ledger-row" style="height:74px">
        <div class="badge badge--olive" style="left:-18px;top:14px">
          <svg width="22" height="22" viewBox="0 0 24 24" fill="none" stroke="#fff" stroke-width="2" stroke-linejoin="round"><path d="M12 3 L22 20 H2 Z"/><path d="M12 9 V14" stroke-linecap="round"/><circle cx="12" cy="17" r=".8" fill="#fff"/></svg>
        </div>
        <div class="fact-cell" style="width:118px;padding-left:40px;padding-top:12px">Material Substitutions Are Risky</div>
        <div class="support-cell"><ul>
          <li>Recent studies show that heavier alternatives to lightweight plastics can significantly increase raw material requirements, energy consumption &amp; landfill volume.</li>
          <li>On a global scale, environmental costing indicates that plastics alternatives may cost $400 to $500 billion more (4 to 5 times more).</li>
          <li>Meat, fish &amp; produce shipped in EPS have a longer shelf life, leading to less food waste.</li>
        </ul></div>
      </div>
      <div class="ledger-row" style="height:60px">
        <div class="badge badge--olive" style="left:-18px;top:10px">
          <svg width="22" height="22" viewBox="0 0 24 24" fill="#fff"><path d="M12 22 V12 C12 7 8 4 3 4 C3 9 6 12 12 12 Z"/><path d="M12 14 C12 9 16 6 21 6 C21 11 18 14 12 14 Z"/><rect x="11" y="12" width="2" height="10"/></svg>
        </div>
        <div class="fact-cell" style="width:118px;padding-left:40px;padding-top:8px">EPS Is More Sustainable Than Most People Imagine</div>
        <div class="support-cell" style="padding-top:8px"><ul>
          <li>EPS foam is of 98% air, which results in lower energy consumption.</li>
          <li>Life cycle analyses show that EPS has far less impact on the environment than other competitive materials for the same use; in particular paper.</li>
        </ul></div>
      </div>
      <div class="ledger-row" style="height:60px">
        <div class="badge badge--olive" style="left:-18px;top:4px">
          <svg width="22" height="22" viewBox="0 0 24 24" fill="#fff"><path d="M6 8 H18 L16.5 22 H7.5 Z"/><rect x="5" y="5.5" width="14" height="1.8"/><rect x="10" y="3" width="4" height="2"/></svg>
        </div>
        <div class="fact-cell" style="width:118px;padding-left:40px;padding-top:8px">Litter Problems Are Not Material Dependent</div>
        <div class="support-cell" style="padding-top:8px"><ul>
          <li>A litter audit in San Francisco confirmed that a food service ban on polystyrene foam only changed the type of litter but did not reduce it.</li>
          <li>Improper disposal of any material contributes to litter, whether it is EPS or another material.</li>
        </ul></div>
      </div>
    </div>
  </div>

  <div class="unit-bg" style="top:386px;width:524px;height:292px"></div>
  <div class="pill pill--brown" style="left:188px;top:404px;width:250px">HUMAN HEALTH &amp; SAFETY</div>
  <div class="ledger" style="left:70px;top:423px;width:486px;--marker:#555">
    <div class="ledger-head" style="height:28px"><span class="col-fact" style="width:119px">FACT</span><span class="col-support">SUPPORTING INFORMATION</span></div>
    <div class="ledger-rows" style="background:#fff">
      <span class="divider" style="left:119px;background:var(--gold)"></span>
      <div class="ledger-row" style="height:78px">
        <div class="badge badge--brown" style="left:-22px;top:12px">
          <svg width="22" height="22" viewBox="0 0 24 24" fill="none" stroke="#fff" stroke-width="2.4" stroke-linecap="round"><circle cx="10" cy="10" r="6.5"/><path d="M15 15 L21 21"/></svg>
        </div>
        <div class="fact-cell" style="width:119px;padding-left:35px;padding-top:16px">There Is Very Little Residual Styrene in EPS.</div>
        <div class="support-cell" style="padding-top:7px"><ul>
          <li>The amount of styrene that might exist in finished polystyrene is extremely small — often lower than naturally occurring styrene found in everyday food items like coffee, strawberries, and cinnamon.</li>
          <li>All chemicals need to be assessed in terms of risk versus exposure. Risks can be zero, negligible or harmful.</li>
        </ul></div>
      </div>
      <div class="ledger-row" style="height:48px">
        <div class="badge badge--brown" style="left:-22px;top:4px">
          <svg width="22" height="22" viewBox="0 0 24 24" fill="#fff" stroke="#fff" stroke-width="1.5"><circle cx="12" cy="12" r="3"/><circle cx="4" cy="6" r="2"/><circle cx="20" cy="7" r="2"/><circle cx="5" cy="19" r="2"/><circle cx="19" cy="19" r="2"/><circle cx="12" cy="3" r="1.5"/><path d="M12 12 L4 6 M12 12 L20 7 M12 12 L5 19 M12 12 L19 19 M12 12 L12 3"/></svg>
        </div>
        <div class="fact-cell" style="width:119px;padding-left:35px;padding-top:8px">EPS Is An Organic Polymer</div>
        <div class="support-cell" style="padding-top:7px"><ul>
          <li>Polystyrene is an organic compound consisting of hydrogen and carbon.</li>
          <li>Polystyrene is chemically very inert, being resistant to acids and bases but is easily dissolved by many chlorinated solvents, and many aromatic hydrocarbon solvents.</li>
        </ul></div>
      </div>
      <div class="ledger-row" style="height:74px">
        <div class="badge badge--brown" style="left:-22px;top:2px">
          <svg width="22" height="22" viewBox="0 0 24 24" fill="none" stroke="#fff" stroke-width="2.2" stroke-linejoin="round" stroke-linecap="round"><rect x="3" y="5" width="16" height="16"/><path d="M7 12 L11 16 L21 4"/></svg>
        </div>
        <div class="fact-cell" style="width:119px;padding-left:35px;padding-top:8px">EPS Is Safe</div>
        <div class="support-cell" style="padding-top:7px"><ul>
          <li>Polystyrene foam is approved for food contact by the FDA and other global regulatory agencies.</li>
          <li>According to the National Oceanic &amp; Atmospheric Administration (NOAA), “although marine debris is a global issue, there are significant gaps in our understanding of the problem.</li>
        </ul></div>
      </div>
    </div>
  </div>

  <footer class="footer">
    <svg class="footer-pin" width="8" height="11" viewBox="0 0 8 11"><path d="M4 0 A4 4 0 0 1 8 4 C8 7 4 11 4 11 C4 11 0 7 0 4 A4 4 0 0 1 4 0 Z" fill="#fff"/><circle cx="4" cy="4" r="1.5" fill="var(--blue)"/></svg>
    <p class="footer-address">Foam Trade Union<br>4470 Meridian Avenue Suite 310<br>Linwood, MD 21077</p>
    <svg class="footer-icons" width="10" height="34" viewBox="0 0 10 34" fill="#fff"><path d="M2 0 L4 0 L5 3 L3.5 4 C4 6 5 7 6.5 7.5 L7.5 6 L10 7 L10 9 C5 9 1 5 1 1 Z"/><rect x="1" y="13" width="8" height="6" rx="1"/><rect x="3" y="11" width="4" height="3"/><circle cx="5" cy="28" r="4.5" fill="none" stroke="#fff" stroke-width="1.2"/><path d="M0.5 28 H9.5 M5 23.5 V32.5" stroke="#fff" stroke-width="1"/></svg>
    <p class="footer-contact">800.555.0142<br>410.555.0187<br>www.foamtradeunion.org</p>
    <span class="social social--a"></span>
    <span class="social social--b"></span>
  </footer>
</section>

</body>
</html>
```